CoinLantern one-page corporate website

Our company, CoinLantern is a cryptocurrency Initial Coin Offering ("ICO" marketing and promotion agency, which requires a professional company landing page design whereby prospective clients can learn;
-who we are
-what we do
-what our people are saying about us
-core team members
-subscribe to our mailing list
-how to get in touch (basic contact form)

We are looking for something unique and attractive -- not a standard Pako template that we could put together ourselves. Plain stock images should not be used. Unique visualizations of the service offerings and creative presentation are key. We are a cutting edge marketing agency and as such, we need to look the part.

Relevant documentation about the business and branding assets have been attached to guide the designer. Certain information will be included by the company at a later date such as team member descriptions. As such, lorem ipsum may be included wherever necessary to help visualize the textual areas.

****Please ensure that you actually utilize the photos and graphics provided so that we can have a good picture of what it would actually look like with our branding.

The site must be responsive HTML CSS Design.

Sites style themes we like for inspiration and specific sections we like ****Very important***:
https://vaultorbitra.example/offers - we like that the token & company logo is used in unique visualizations that connects various ideas together. We imagine unique visuals such as these with our Icon (see attached) serving as a token. We also like the unique and attractive visual theme of the webpage itself.

https://quarrelstone.example/ - we like the layout of this website, specifically how the service offerings are displayed in a circular visual graphic with the Quarrel logo in the middle. We imagine a similar type of graphic designed with CoinLantern in the middle.

https://zorvinet.example/ - we like how the logo is central to the theme in this site when you first enter and how it fades + shrinks into the distance as you scroll down.

Target Market(s)

cryptocurrency entrepreneurs and ICOs

Industry/Entity Type

It Company

Coding

Coded - Design and coding required

Number of Pages Required

1 page

Font styles to use
Sans Serif

Colors

Designer to choose colors to be used in the design.

Requirements
Must have
• The site must be responsive HTML CSS Design.
• The page must be modern and visually attractive. Elements must not be static and should have a fluid motion / visual change as the user scrolls through the page.
Should not have
• The project should not use any old stock images or elements which are dull and over-used, but rather images or elements should be unique and well thought out.

```html
<!DOCTYPE html>
<html lang="en">
<head>
<meta charset="utf-8">
<title>CoinLantern – The Token Sale Experts</title>
<link href="https://fonts.googleapis.com/css2?family=Montserrat:wght@400;500;600;700&family=Open+Sans:wght@400;600&display=swap" rel="stylesheet">
<style>
:root{
  --blue:#1a8ad8;
  --blue-deep:#0b6db5;
  --blue-light:#5fb3ea;
  --ink:#1d2530;
  --text:#5b6470;
  --muted:#9aa2ac;
  --teal-a:#2f9e9b;
  --teal-b:#1e7a88;
  --grey-bg:#eef0f3;
  --footer:#0d4f86;
  --white:#ffffff;
}
*{margin:0;padding:0;box-sizing:border-box}
html,body{width:1200px;height:4091px;overflow:hidden}
body{position:relative;background:var(--white);font-family:"Open Sans",Arial,sans-serif;color:var(--text)}
.abs{position:absolute}
.center{left:0;width:1200px;text-align:center}
h1,h2,h3,h4{font-family:"Montserrat",Arial,sans-serif}
.btn{position:absolute;display:block;background:var(--blue);color:var(--white);font-family:"Montserrat",Arial,sans-serif;font-size:13px;border-radius:20px;text-align:center;line-height:32px;height:32px}

/* hero */
.hero{position:absolute;left:0;top:0;width:1200px;height:627px;
  clip-path:polygon(0 0,100% 0,100% 520px,50% 627px,0 520px);
  background:linear-gradient(180deg,#cfd7e0 0%,#8a98a8 40%,#4d5a6a 75%,#2d3845 100%)}
.hero-shade{position:absolute;inset:0;background:radial-gradient(ellipse at 50% 30%,rgba(255,255,255,.45),rgba(255,255,255,0) 60%)}
.burger{position:absolute;left:96px;top:56px;width:24px}
.burger span{display:block;height:3px;background:var(--ink);margin-bottom:4px}
.brand{position:absolute;display:flex;align-items:center;gap:16px;font-family:"Montserrat",Arial,sans-serif;font-weight:600;color:var(--blue-deep)}
.brand-dot{border:6px solid var(--blue-deep);border-radius:50%}
.hero .brand{left:382px;top:140px;font-size:56px}
.hero .brand-dot{width:70px;height:70px}
.hero-title{top:330px;font-size:44px;font-weight:700;color:var(--white);letter-spacing:1px}
.hero-sub{top:395px;font-size:14px;font-weight:600;color:var(--white);text-transform:uppercase}
.hero-btn{left:536px;top:450px;width:128px}

/* who we are */
.logo-card{position:absolute;left:150px;top:690px;width:392px;height:112px;border:2px solid #9fd0f2;box-shadow:0 0 14px rgba(26,138,216,.45);background:linear-gradient(#fff,#eef2f6);text-align:center}
.logo-card .name{font-family:"Montserrat",Arial,sans-serif;font-weight:600;font-size:46px;color:var(--blue-deep);margin-top:12px}
.logo-card .tag{font-family:"Montserrat",Arial,sans-serif;font-size:18px;color:var(--muted);margin-top:-4px}
.token-art{position:absolute;left:190px;top:832px;width:310px;height:128px;border-radius:64px;background:linear-gradient(90deg,#dcebf7,#b9d8f0 50%,#dcebf7)}
.who-title{left:652px;top:700px;font-size:42px;font-weight:700;color:var(--ink)}
.who-text{left:655px;top:768px;width:360px;font-size:12px;line-height:21px;color:#333}
.who-btn{left:657px;top:918px;width:118px}

/* cost */
.cost-bg{position:absolute;left:0;top:1017px;width:1200px;height:600px;background:linear-gradient(90deg,#f4f4f4,#e9e9e9 60%,#e2e2e2)}
.hand{position:absolute;left:960px;top:1260px;width:240px;height:357px;background:linear-gradient(135deg,#e8c7ae,#b78a70 50%,#d7d0cc);clip-path:polygon(10% 0,40% 5%,100% 45%,100% 100%,30% 100%,0 20%)}
.cost-title{top:1070px;font-size:30px;font-weight:600;color:#222}
.cost-text{left:160px;width:880px;top:1115px;font-size:13px;line-height:22px;text-align:center;color:#444}
.svc{position:absolute;font-family:"Montserrat",Arial,sans-serif}
.svc h4{font-size:20px;font-weight:600;color:#222}
.svc p{font-size:11px;color:#666;margin-top:2px}
.svc.l{text-align:right}
.svc-icon{position:absolute;width:64px;height:64px;border-radius:50%;background:var(--white);box-shadow:0 2px 8px rgba(0,0,0,.12);display:flex;align-items:center;justify-content:center}
.hub{position:absolute;left:518px;top:1331px;width:136px;height:136px;border-radius:50%;background:var(--white);box-shadow:0 4px 16px rgba(0,0,0,.15)}
.hub-fill{position:absolute;left:28px;top:28px;width:80px;height:80px;border-radius:50%;background:linear-gradient(135deg,#cfe4f5,#8fc1e8)}

/* how it works */
.how-ghost{top:1650px;font-family:"Montserrat",Arial,sans-serif;font-size:56px;font-weight:700;color:#f3f4f6}
.how-title{top:1680px;font-size:30px;font-weight:400;color:#222}
.rule{position:absolute;height:3px;background:var(--blue)}
.step{position:absolute;width:260px;text-align:center}
.step h4{font-size:13px;font-weight:700;color:#222}
.step p{font-size:11px;line-height:20px;color:#777;margin-top:10px}

/* cta */
.cta-art{position:absolute;left:0;top:0}
.cta-head{left:98px;top:2136px;font-size:24px;font-weight:700;color:#111;white-space:nowrap}
.cta-sub{left:98px;top:2180px;font-family:"Montserrat",Arial,sans-serif;font-size:17px;color:#333;white-space:nowrap}
.cta-text{left:98px;top:2218px;width:650px;font-size:12px;line-height:21px;color:#666}
.contact-us{left:915px;top:2160px;font-family:"Montserrat",Arial,sans-serif;font-size:34px;color:var(--white)}
.phone{left:915px;top:2207px;font-family:"Montserrat",Arial,sans-serif;font-size:32px;font-weight:700;color:var(--white)}

/* testimonials */
.testi{position:absolute;left:0;top:2326px;width:1200px;height:420px;background:linear-gradient(135deg,var(--teal-a),var(--teal-b))}
.testi-title{top:2370px;font-size:30px;font-weight:700;color:var(--white)}
.avatar{position:absolute;left:532px;top:2444px;width:136px;height:136px;border-radius:50%;border:4px solid var(--white);background:linear-gradient(#dfe4ea,#2c3746)}
.testi-text{left:250px;width:700px;top:2592px;font-size:13px;line-height:24px;text-align:center;color:var(--white)}
.testi-name{top:2690px;font-family:"Montserrat",Arial,sans-serif;font-size:13px;font-weight:700;color:var(--white)}
.arrow{position:absolute}

/* experts */
.exp-title{top:2800px;font-size:26px;font-weight:700;color:#111}
.exp-text{left:270px;width:660px;top:2862px;font-size:11px;line-height:20px;text-align:center;color:#777}
.card{position:absolute;width:215px;text-align:center}
.card .photo{height:252px;box-shadow:0 2px 8px rgba(0,0,0,.15)}
.card h4{font-size:13px;font-weight:700;color:#111;margin-top:22px}
.card small{display:block;font-size:9px;color:#888;margin-top:2px}
.socials{display:flex;justify-content:center;gap:10px;margin-top:8px}
.socials i{width:9px;height:9px;border-radius:50%;background:#333}

/* newsletter */
.news{position:absolute;left:0;top:3305px;width:1200px;height:290px;background:linear-gradient(90deg,var(--blue-deep),var(--blue) 60%,#2e9ae0);clip-path:polygon(0 0,100% 0,100% 86%,50% 100%,0 86%)}
.news-title{top:3340px;font-size:40px;font-weight:600;color:var(--white)}
.news-sub{top:3398px;font-size:14px;color:#d6ebfa}
.news-input{position:absolute;left:305px;top:3441px;width:437px;height:50px;background:var(--white);font-size:12px;color:#aaa;padding:16px 14px}
.news-btn{position:absolute;left:750px;top:3441px;width:114px;height:50px;border:1px solid var(--white);color:var(--white);font-size:13px;text-align:center;line-height:48px}
.news-note{top:3518px;font-size:13px;color:#d6ebfa}

/* contact */
.contact{position:absolute;left:0;top:3594px;width:1200px;height:437px;background:var(--grey-bg)}
.contact-title{top:3642px;font-size:30px;font-weight:600;color:#111;letter-spacing:1px}
.person{position:absolute;left:0;top:3695px;width:300px;height:336px;background:linear-gradient(180deg,#e6d2c2,#b78a6e 40%,#f1f1f1 60%,#dcdcdc)}
.field{position:absolute;font-size:11px;color:#888;border-bottom:1px solid #c9ccd1;padding-bottom:8px}
.field.active{color:var(--blue);border-bottom:2px solid var(--blue)}
.message{position:absolute;left:349px;top:3826px;width:507px;height:95px;border:1px solid #c9ccd1;font-size:11px;color:#888;padding:8px 10px}
.contact-btn{left:537px;top:3963px;width:118px}
.deco{position:absolute;border-radius:10px}

footer{position:absolute;left:0;top:4031px;width:1200px;height:60px;background:var(--footer);color:#b9d3ea;font-size:11px;text-align:center;line-height:60px}
</style>
</head>
<body>

<!-- HERO -->
<section class="hero">
  <div class="hero-shade" role="img" aria-label="Upward view of glass office towers against a pale sky"></div>
  <div class="burger"><span></span><span></span><span></span></div>
  <div class="brand"><i class="brand-dot"></i>CoinLantern</div>
  <h1 class="abs center hero-title">WELCOME TO COINLANTERN</h1>
  <p class="abs center hero-sub">Our experts will ensure that your ICO is run properly, communicated well, and achieves your desired outcomes</p>
  <a class="btn hero-btn">Know More...</a>
</section>

<!-- WHO WE ARE -->
<section class="who">
  <div class="logo-card"><div class="name">CoinLantern</div><div class="tag">The Token Sale Experts</div></div>
  <div class="token-art" role="img" aria-label="Illustration of the brand token beside a coin and a stack of coins"></div>
  <h2 class="abs who-title">WHO WE ARE</h2>
  <p class="abs who-text">Lorem ipsum dolor sit amet, consectetur adipiscing elit. Duis hendrerit dolor quis diam gravida, eget semper purus auctor. Praesent et magna erat. Suspendisse orci libero, egestas efficitur metus ut, volutpat mollis enim. Vestibulum sollicitudin, nibh vitae finibus tincidunt, orci diam rhoncus sapien, sed dignissim velit mi non nunc.</p>
  <a class="btn who-btn">Read More...</a>
</section>

<!-- HOW MUCH DOES IT COST -->
<section class="cost">
  <div class="cost-bg" role="img" aria-label="Soft white painted brick wall"></div>
  <div class="hand" role="img" aria-label="Hand in a suit sleeve pointing at the service graphic"></div>
  <h2 class="abs center cost-title">HOW MUCH DOES IT COST?</h2>
  <p class="abs cost-text">Every Token sale is unique, that is why CoinLantern begins with a one-on-one conversation to identify your specific needs and agree upon terms that make sense for all parties. We structure engagements according to the principle of aligned interests - our success is your success and vice versa</p>

  <div class="svc l" style="right:815px;top:1240px"><h4>Duis accumsan</h4><p>Morbi mollis turpis eget ligula vestibulum</p></div>
  <div class="svc l" style="right:865px;top:1370px"><h4>Auis cumsan</h4><p>Morbi mollis turpis eget ligula</p></div>
  <div class="svc l" style="right:815px;top:1510px"><h4>Euis sumsan</h4><p>Morbi mollis turpis eget ligula</p></div>
  <div class="svc" style="left:769px;top:1234px"><h4>Duis accumsan</h4><p>Morbi mollis turpis eget ligula vestibulum</p></div>
  <div class="svc" style="left:826px;top:1370px"><h4>Auis cumsan</h4><p>Morbi mollis turpis eget ligula</p></div>
  <div class="svc" style="left:780px;top:1510px"><h4>Euis sumsan</h4><p>Morbi mollis turpis eget ligula</p></div>

  <div class="svc-icon" style="left:413px;top:1238px"><svg width="30" height="30" viewBox="0 0 30 30" fill="none" stroke="#555" stroke-width="2"><circle cx="15" cy="13" r="9"/><path d="M15 22v6M10 28h10"/></svg></div>
  <div class="svc-icon" style="left:363px;top:1370px"><svg width="28" height="30" viewBox="0 0 28 30" fill="none" stroke="#555" stroke-width="2"><ellipse cx="14" cy="6" rx="10" ry="4"/><path d="M4 6v18c0 2 4 4 10 4s10-2 10-4V6M4 12c0 2 4 4 10 4s10-2 10-4M4 18c0 2 4 4 10 4s10-2 10-4"/></svg></div>
  <div class="svc-icon" style="left:410px;top:1505px"><svg width="24" height="30" viewBox="0 0 24 30" fill="none" stroke="#555" stroke-width="2"><path d="M2 2h14l6 6v20H2z"/><path d="M6 14h12M6 19h12M6 24h8"/></svg></div>
  <div class="svc-icon" style="left:677px;top:1234px"><svg width="30" height="30" viewBox="0 0 30 30" fill="none" stroke="#555" stroke-width="2"><circle cx="12" cy="12" r="9"/><path d="M19 19l9 9"/></svg></div>
  <div class="svc-icon" style="left:740px;top:1370px"><svg width="30" height="30" viewBox="0 0 30 30" fill="none" stroke="#555" stroke-width="2"><circle cx="15" cy="15" r="5"/><circle cx="15" cy="15" r="11" stroke-dasharray="4 3"/></svg></div>
  <div class="svc-icon" style="left:691px;top:1505px"><svg width="30" height="30" viewBox="0 0 30 30" fill="#555"><rect x="3" y="16" width="4" height="12"/><rect x="10" y="10" width="4" height="18"/><rect x="17" y="13" width="4" height="15"/><rect x="24" y="6" width="4" height="22"/></svg></div>

  <div class="hub"><div class="hub-fill" role="img" aria-label="Brand token icon at the centre of the services"></div></div>
</section>

<!-- HOW IT WORKS -->
<section class="how">
  <div class="abs center how-ghost">STEPS</div>
  <h2 class="abs center how-title">How it works</h2>
  <div class="rule" style="left:558px;top:1730px;width:84px"></div>

  <svg class="abs" style="left:0;top:1820px" width="1200" height="100" viewBox="0 0 1200 100" aria-hidden="true">
    <g fill="none" stroke="#1a8ad8" stroke-width="2">
      <circle cx="270" cy="48" r="34"/><circle cx="597" cy="48" r="34"/><circle cx="924" cy="48" r="34"/>
      <path d="M256 48l10 10 18-20"/>
      <rect x="585" y="32" width="24" height="32" rx="2"/><path d="M591 42h12M591 50h12M591 57h8"/>
      <circle cx="924" cy="48" r="14"/><path d="M918 52q6 6 12 0"/><path d="M919 44h1M929 44h1"/>
      <path d="M360 38q100-40 190 0" stroke-dasharray="6 6"/><path d="M540 30l10 8-12 3"/>
      <path d="M687 38q100-40 190 0" stroke-dasharray="6 6"/><path d="M867 30l10 8-12 3"/>
    </g>
    <g fill="#1a8ad8"><circle cx="296" cy="20" r="9"/><circle cx="623" cy="20" r="9"/><circle cx="950" cy="20" r="9"/></g>
    <g fill="#fff" font-family="Montserrat, sans-serif" font-size="10" text-anchor="middle"><text x="296" y="24">1</text><text x="623" y="24">2</text><text x="950" y="24">3</text></g>
  </svg>

  <div class="step" style="left:140px;top:1928px"><h4>LOREM IPSUM</h4><p>Capitalize on low hanging fruit to identify a ballpark value added activity to beta test.</p></div>
  <div class="step" style="left:467px;top:1928px"><h4>DOLOR AMIT SQUET</h4><p>Capitalize on low hanging fruit to identify a ballpark value added activity to beta test.</p></div>
  <div class="step" style="left:794px;top:1928px"><h4>IPSUM DOLOR VENTUE</h4><p>Capitalize on low hanging fruit to identify a ballpark value added activity to beta test.</p></div>
</section>

<!-- CALL TO ACTION -->
<section class="cta">
  <svg class="cta-art" width="1200" height="2330" viewBox="0 0 1200 2330" aria-hidden="true">
    <polygon points="760,2072 1200,2072 1200,2255 845,2255" fill="#1a8ad8"/>
    <polygon points="1000,2255 1200,2255 1200,2326" fill="#5fb3ea"/>
  </svg>
  <h3 class="abs cta-head">LOREM IPSUM DOLOR , CONSECTETUR ADIPISCING ELIT.</h3>
  <p class="abs cta-sub">GRAVIDA, EGET SEMPER PURUS AUCTOR. PRAESENT ET MAGNA ERAT</p>
  <p class="abs cta-text">Duis hendrerit dolor quis diam gravida, eget semper purus auctor. Praesent et magna erat. Suspendisse orci libero, egestas efficitur metus ut, volutpat mollis enim. Vestibulum sollicitudin, nibh vitae finibus tincidunt,</p>
  <div class="abs contact-us">CONTACT US</div>
  <div class="abs phone">1800-555-0142</div>
</section>

<!-- TESTIMONIALS -->
<section>
  <div class="testi"></div>
  <h2 class="abs center testi-title">WHAT OUR PEOPLE ARE SAYING ABOUT US</h2>
  <div class="avatar" role="img" aria-label="Portrait photo of the client giving the testimonial"></div>
  <p class="abs testi-text">Lorem ipsum dolor sit amet, consectetur adipiscing elit. Duis hendrerit dolor quis diam gravida, eget semper purus auctor. Praesent et magna erat. Suspendisse orci libero, egestas efficitur metus ut, volutpat mollis enim. Vestibulum sollicitudin, nibh vitae finibus tincidunt,</p>
  <div class="abs center testi-name">|- JON RIVEL</div>
  <svg class="arrow" style="left:100px;top:2525px" width="20" height="44" viewBox="0 0 20 44"><path d="M18 2L2 22l16 20" fill="none" stroke="#fff" stroke-width="2"/></svg>
  <svg class="arrow" style="left:1080px;top:2525px" width="20" height="44" viewBox="0 0 20 44"><path d="M2 2l16 20L2 42" fill="none" stroke="#fff" stroke-width="2"/></svg>
</section>

<!-- EXPERTS -->
<section>
  <h2 class="abs center exp-title">MEET OUR EXPERTS</h2>
  <div class="rule" style="left:570px;top:2845px;width:60px"></div>
  <p class="abs exp-text">Lorem ipsum dolor sit amet consectetur adipiscing elit sed eiusmod tempor enim minim veniam quis nostrud exercit ation Lorem ipsum dolor sit amet dictum quis nostra exercit.</p>
  <svg class="arrow" style="left:102px;top:3050px" width="14" height="40" viewBox="0 0 14 40"><path d="M12 2L2 20l10 18" fill="none" stroke="#555" stroke-width="2"/></svg>
  <svg class="arrow" style="left:1084px;top:3050px" width="14" height="40" viewBox="0 0 14 40"><path d="M2 2l10 18L2 38" fill="none" stroke="#555" stroke-width="2"/></svg>

  <div class="card" style="left:183px;top:2945px">
    <div class="photo" role="img" aria-label="Team member standing at a conference stand" style="background:linear-gradient(135deg,#e8eef4,#3a8fd6 45%,#5b4a40 75%,#dfe4ea)"></div>
    <h4>NED ORRIN</h4><small>LOREM IPSUM DOLOR</small><div class="socials"><i></i><i></i><i></i></div>
  </div>
  <div class="card" style="left:483px;top:2945px">
    <div class="photo" role="img" aria-label="Team member standing beside a red sports car" style="background:linear-gradient(180deg,#a9c6e2,#d8d2c4 40%,#d9c43a 60%,#a8262a 85%)"></div>
    <h4>TAVO BRISK</h4><small>LOREM IPSUM DOLOR</small><div class="socials"><i></i><i></i><i></i></div>
  </div>
  <div class="card" style="left:785px;top:2945px">
    <div class="photo" role="img" aria-label="Team member portrait in sunglasses" style="background:linear-gradient(135deg,#f2f2f2,#8b6a4f 45%,#2f2a28 75%,#e6e6e6)"></div>
    <h4>LUCAN MERROW</h4><small>LOREM IPSUM DOLOR</small><div class="socials"><i></i><i></i><i></i></div>
  </div>
</section>

<!-- NEWSLETTER -->
<section>
  <div class="news"></div>
  <h2 class="abs center news-title">Want to know more?</h2>
  <p class="abs center news-sub">Subscribe to our newsletter</p>
  <div class="news-input">Enter Email</div>
  <div class="news-btn">Submit</div>
  <p class="abs center news-note">Dont worry about spam. We hate spam too. You will receive only one mail per month.</p>
</section>

<!-- CONTACT -->
<section>
  <div class="contact"></div>
  <div class="deco" style="left:940px;top:3640px;width:180px;height:160px;background:rgba(95,163,220,.45)"></div>
  <div class="deco" style="left:1050px;top:3730px;width:150px;height:160px;background:rgba(95,163,220,.35)"></div>
  <div class="deco" style="left:935px;top:3820px;width:160px;height:140px;background:rgba(95,163,220,.25)"></div>
  <div class="deco" style="left:1035px;top:3880px;width:165px;height:150px;background:rgba(95,163,220,.3)"></div>
  <h2 class="abs center contact-title">HOW TO GET IN TOUCH</h2>
  <div class="rule" style="left:566px;top:3685px;width:68px"></div>
  <div class="person" role="img" aria-label="Smiling man in glasses pointing toward the contact form"></div>
  <div class="field active" style="left:349px;top:3733px;width:235px">NAME</div>
  <div class="field" style="left:622px;top:3733px;width:234px">EMAIL</div>
  <div class="field" style="left:349px;top:3777px;width:235px">SUBJECT</div>
  <div class="field" style="left:622px;top:3777px;width:234px">PHONE NUMBER</div>
  <div class="message">MESSAGE</div>
  <a class="btn contact-btn">SUBMIT</a>
</section>

<footer>copyright 2017-2018</footer>
</body>
</html>
```